Ferncrest Dental, LLC business card project

Business card to be designed with current logo.
Dental office- please keep design of card that looks clean and professional.
Please include the following info:
Ferncrest Dental, LLC
Dr. Lorna Pettigrew
2871 Marlowe Street
Millbrook Glen, VT 05699
802-555-0193
ferncrestdental.office@examplemail.test
Hello everyone-
Reason: Just got back from overseas- will look at all designs and provide feedback. Thank you!
Reason: Polling my friends for the final selection-
thank you to all those that participated- so many talented designers!

```html
<!DOCTYPE html>
<html lang="en">
<head>
<meta charset="utf-8">
<title>Ferncrest Dental, LLC — Business Card</title>
<link rel="stylesheet" href="https://fonts.googleapis.com/css2?family=Marcellus&display=swap">
<style>
  :root {
    --backdrop: #ecebe8;
    --card-light: #f4f4f4;
    --card-mid: #c9c9c9;
    --card-shade: #8e8e8e;
    --band: #0d1013;
    --brand-green: #9ee21e;
    --name-blue: #5b84e6;
    --contact-white: #f5f5f5;
  }
  * { margin: 0; padding: 0; box-sizing: border-box; }
  html, body { width: 922px; height: 1200px; overflow: hidden; }
  body {
    background: var(--backdrop);
    font-family: "Marcellus", serif;
    position: relative;
  }
  .business-card {
    position: absolute;
    left: 51px; top: 190px;
    width: 820px; height: 470px;
    border-radius: 16px;
    overflow: hidden;
    background: linear-gradient(180deg, var(--card-light) 0%, var(--card-mid) 30%, var(--card-light) 50%, var(--card-shade) 80%, var(--card-light) 100%);
    box-shadow: 0 6px 22px rgba(0,0,0,.18);
  }
  .business-card .band { position: absolute; inset: 0; }
  .card-brand {
    position: absolute; right: 40px; top: 36px;
    display: flex; align-items: center; gap: 12px;
    color: var(--brand-green);
    font-size: 40px; line-height: 1;
  }
  .brand-dot {
    width: 30px; height: 30px; border-radius: 50%;
    background: var(--brand-green);
  }
  .practice {
    position: absolute; left: 40px; top: 214px;
    color: var(--name-blue);
  }
  .practice-name { font-size: 29px; line-height: 1.1; }
  .practice-doctor { font-size: 22px; margin-top: 12px; margin-left: 18px; }
  .contact {
    position: absolute; left: 400px; top: 228px;
    color: var(--contact-white);
    font-size: 19px; line-height: 1.35;
    list-style: none;
  }
  .contact li { margin-bottom: 16px; }
  .contact .label { display: inline-block; width: 30px; }
  .contact .indent { padding-left: 30px; display: block; }
  .contact .email { font-size: 16px; }
  .brand-lockup {
    position: absolute; left: 0; right: 0; top: 800px;
    display: flex; align-items: center; justify-content: center; gap: 20px;
    color: var(--brand-green);
    font-size: 70px; line-height: 1;
  }
  .brand-lockup .brand-dot { width: 56px; height: 56px; }
</style>
</head>
<body>
  <section class="business-card" aria-label="Ferncrest Dental business card">
    <svg class="band" width="820" height="470" viewBox="0 0 820 470" aria-hidden="true">
      <polygon fill="#0d1013" points="0,131 270,131 369,207 820,207 820,409 369,409 270,338 0,338"/>
    </svg>
    <div class="card-brand"><span class="brand-dot"></span><span>Ferncrest Dental, LLC</span></div>
    <div class="practice">
      <p class="practice-name">Ferncrest Dental, LLC</p>
      <p class="practice-doctor">Dr. Lorna Pettigrew</p>
    </div>
    <ul class="contact">
      <li><span class="label">H-</span>2871 Marlowe Street<span class="indent">Millbrook Glen, VT 05699</span></li>
      <li class="email"><span class="label">E-</span>ferncrestdental.office@examplemail.test</li>
      <li><span class="label">P-</span>802-555-0193</li>
    </ul>
  </section>
  <div class="brand-lockup"><span class="brand-dot"></span><span>Ferncrest Dental, LLC</span></div>
</body>
</html>
```